electrical company- Company name- Voltmark Trades, slogan- All installations and servicingcolours to stick roughly with logo- greys, blues, black, white. simple yet effective- logo to stand out and attention to name also (gareth). Modern design.

Industry/Entity Type

Business

Contact Information for Business Card

gareth WilliamsElectrician021 994 306info@voltmarktrades.co.nzwww.voltmarktrades.co.nzPO box 5367Palmerston North, 4472

```html
<!DOCTYPE html>
<html lang="en">
<head>
<meta charset="utf-8">
<title>Voltmark Trades – Business Card</title>
<link href="https://fonts.googleapis.com/css2?family=Poppins:wght@600&family=Questrial&display=swap" rel="stylesheet">
<style>
  :root {
    --backdrop: #a3a8a3;
    --card: #ffffff;
    --brand-blue: #1e8fd0;
    --brand-grey: #6f7072;
    --ink: #1c1c1c;
    --rule: #8a8a8a;
  }
  * { box-sizing: border-box; margin: 0; padding: 0; }
  html, body {
    width: 1200px;
    height: 1072px;
    overflow: hidden;
  }
  body {
    background: var(--backdrop);
    display: flex;
    align-items: center;
    justify-content: center;
    font-family: "Questrial", "Century Gothic", sans-serif;
    color: var(--ink);
  }
  .business-card {
    position: relative;
    width: 1000px;
    height: 572px;
    background: var(--card);
    box-shadow: 0 18px 40px rgba(0,0,0,0.18);
  }
  .brand {
    position: absolute;
    left: 0;
    top: 0;
    width: 560px;
    height: 100%;
    display: flex;
    align-items: center;
    justify-content: center;
    gap: 20px;
  }
  .brand-mark {
    width: 64px;
    height: 64px;
    background: var(--brand-blue);
    flex: none;
  }
  .brand-name {
    font-family: "Questrial", "Century Gothic", sans-serif;
    font-size: 42px;
    color: var(--brand-grey);
    letter-spacing: 0.5px;
    white-space: nowrap;
  }
  .divider {
    position: absolute;
    left: 560px;
    top: 175px;
    width: 2px;
    height: 250px;
    background: linear-gradient(to bottom, rgba(138,138,138,0), var(--rule) 20%, var(--rule) 80%, rgba(138,138,138,0));
  }
  .contact {
    position: absolute;
    left: 612px;
    top: 170px;
  }
  .contact-name {
    font-family: "Poppins", "Century Gothic", sans-serif;
    font-weight: 600;
    font-size: 27px;
    line-height: 1.1;
    color: var(--brand-blue);
  }
  .contact-role {
    font-size: 21px;
    line-height: 1.2;
    margin-left: 8px;
  }
  .contact-address {
    font-size: 22px;
    line-height: 1.35;
    margin: 22px 0 0 22px;
  }
  .contact-lines {
    list-style: none;
    margin: 20px 0 0 40px;
    font-size: 22px;
    line-height: 1.45;
  }
  .contact-lines li {
    display: flex;
    align-items: center;
    gap: 14px;
  }
  .contact-icon {
    width: 22px;
    height: 22px;
    flex: none;
    fill: var(--brand-blue);
  }
</style>
</head>
<body>
  <article class="business-card">
    <div class="brand">
      <span class="brand-mark" aria-hidden="true"></span>
      <span class="brand-name">Voltmark Trades</span>
    </div>

    <div class="divider" aria-hidden="true"></div>

    <section class="contact">
      <h1 class="contact-name">Gareth Pemberly</h1>
      <p class="contact-role">Electrician</p>
      <p class="contact-address">PO Box 8142<br>Ashvale North, 4472</p>
      <ul class="contact-lines">
        <li>
          <svg class="contact-icon" viewBox="0 0 24 24" aria-hidden="true">
            <path d="M2 9c0-3 4-5 10-5s10 2 10 5v2h-5V9c-1-.6-3-1-5-1s-4 .4-5 1v2H2z"/>
            <path d="M6 13l2-3h8l2 3v7H6z"/>
          </svg>
          021 573 814
        </li>
        <li>
          <svg class="contact-icon" viewBox="0 0 24 24" aria-hidden="true">
            <path d="M2 5h20v14H2z M4 7v.4l8 6 8-6V7z" fill-rule="evenodd"/>
          </svg>
          info@voltmarktrades-example.co.nz
        </li>
        <li>
          <svg class="contact-icon" viewBox="0 0 24 24" aria-hidden="true">
            <circle cx="12" cy="12" r="10"/>
            <path d="M12 2v20M2 12h20M5 6c4 2 10 2 14 0M5 18c4-2 10-2 14 0" stroke="#fff" stroke-width="1.3" fill="none"/>
          </svg>
          www.voltmarktrades-example.co.nz
        </li>
      </ul>
    </section>
  </article>
</body>
</html>
```